i would like a business card to leave with customers and potential customers for electrical work and for the supply and install of reverse cycle airconditioning in the domestic and commercial market.
I own my own business and im a sole trader. I have an a'class electrical lisence and also a refrigeration lisence so i am
able to offer complete installations in airconditioning by a fully qualified and lisenced tradesman.
im looking for something that comes across as unique and professional.
i had the coluor black and some gold in mind but open to any coluors.
something like Brightline Electrical & Refrigeration
or Brightline Air.
i will use this design on a business card to advertise through summer to help generate installs through the busy season.

Target Market(s)

Mainly domestic house holds through summer who are in need of airconditioning and reliable information to acomadate thier cooling and heating requirements

Industry/Entity Type

Electrical

Requirements
Must have
• Business name- Brightline
My name- Peter Mulvane
My mobile no- 0438 517 209
My email- rtmulvane@kestrelnet.com.au
Installation & Decomissioning of aiconditioning split systems
LIC NO: TKR 504613
Nice to have
• Brightline Electrical & Refrigeration

```html
<!DOCTYPE html>
<html lang="en">
<head>
<meta charset="utf-8">
<title>Brightline Electrical &amp; Refrigeration – Business Card</title>
<link rel="stylesheet" href="https://fonts.googleapis.com/css2?family=Arimo:wght@400;700&display=swap">
<style>
  :root {
    --card-black: #0d0c0b;
    --gold: #e7c21c;
    --white: #f4f4f4;
    --backdrop: #e4e4e4;
  }
  * { margin: 0; padding: 0; box-sizing: border-box; }
  html, body { width: 1200px; height: 951px; overflow: hidden; }
  body {
    background: var(--backdrop);
    font-family: "Arimo", Arial, sans-serif;
    position: relative;
  }
  .card {
    position: absolute;
    width: 640px;
    height: 370px;
    background: var(--card-black);
    border-radius: 18px;
    color: var(--white);
  }
  .card--front { left: 90px; top: 70px; }
  .card--back { left: 470px; top: 510px; }

  /* Front */
  .front-name {
    position: absolute;
    left: 70px; top: 95px;
    display: flex; align-items: center; gap: 22px;
  }
  .brand-square { width: 70px; height: 70px; background: var(--gold); flex: none; }
  .front-name .brand-word {
    font-size: 84px; font-weight: 700; color: var(--gold); letter-spacing: -1px;
  }
  .front-tagline {
    position: absolute;
    left: 56px; top: 282px;
    font-size: 25px; font-weight: 400; color: var(--gold);
    text-transform: uppercase; letter-spacing: 0.3px;
  }

  /* Back */
  .back-brand {
    position: absolute;
    left: 26px; top: 156px;
    display: flex; align-items: center; gap: 12px;
  }
  .back-brand .brand-square { width: 32px; height: 32px; }
  .back-brand .brand-word {
    font-size: 32px; font-weight: 700; color: var(--gold); text-transform: uppercase;
  }
  .divider {
    position: absolute;
    left: 320px; top: 40px;
    width: 2px; height: 290px;
    background: var(--gold);
  }
  .contact { position: absolute; left: 342px; top: 58px; }
  .contact-name { font-size: 31px; font-weight: 400; color: var(--gold); margin-bottom: 16px; }
  .contact-line { font-size: 16px; line-height: 1.45; }
  .licence {
    position: absolute; left: 342px; top: 232px;
    display: flex; gap: 12px; align-items: flex-start;
  }
  .licence-badge { width: 40px; height: 46px; flex: none; margin-top: 4px; }
  .licence-text { font-size: 15px; line-height: 1.3; }
</style>
</head>
<body>
  <section class="card card--front" aria-label="Business card front">
    <div class="front-name">
      <span class="brand-square"></span>
      <span class="brand-word">Brightline</span>
    </div>
    <p class="front-tagline">Brightline Electrical &amp; Refrigeration</p>
  </section>

  <section class="card card--back" aria-label="Business card back">
    <div class="back-brand">
      <span class="brand-square"></span>
      <span class="brand-word">Brightline</span>
    </div>
    <div class="divider"></div>
    <div class="contact">
      <p class="contact-name">Peter Mulvane</p>
      <p class="contact-line">m: 0438 517 209</p>
      <p class="contact-line">e: rtmulvane@kestrelnet.com.au</p>
    </div>
    <div class="licence">
      <svg class="licence-badge" viewBox="0 0 40 46" aria-hidden="true">
        <rect x="1.5" y="1.5" width="37" height="43" fill="none" stroke="#f4f4f4" stroke-width="3"/>
      </svg>
      <p class="licence-text">LIC NO: TKR 504613<br>Installation &amp; Decomissioning<br>of aiconditioning split systems</p>
    </div>
  </section>
</body>
</html>
```